I am looking for a flyer design for my upcoming symposium. Here are the details for the flyer and pictures of speakers are attached.

Name of Symposium: Lattice and Pathway Biosciences Symposium, Sponsored by the Corvale Chromatin Institute and the Department of Bioengineering
Date: January 8, 2018
Location: Havergill Auditorium, Tarnby Center for Applied Discovery, 2175 Orchard Terrace Ave, Philadelphia, PA 19127

Reception to follow after the symposium.

Also, please add - Register and upload abstracts for the symposium at www.qzvmrk.com. Registration and abstract submission closes on January 4, 2018.

Keynote Speaker:
Marthe Quillon, Ph.D.
NTVO Director General; Professor, Lyceum of Norvane; Director, Genetics and Developmental Biology at Institut Bramoux
Lyceum of Norvane, NTVO, Institut Bramoux
"Title of talk TBA."

Speakers:
Lena Drewcott, Ph.D.
Assistant Professor of Cell and Developmental Biology
Halvering State University, HMCS
"Title of talk TBA."

Paul Marden, Ph.D.
Assistant Professor of Genetics
"Title of talk TBA."

Ilse Varga, Ph.D.
Professor, Ostrander University
Otto Wenzlau Center for Molecular Medicine
"Title of talk TBA."

Jun Hao, Ph.D.
Professor of Cellular and Molecular Medicine
Coastal Meridian University
"Title of talk TBA."

Wei Lun, Ph.D.
Associate Professor of Pediatrics
The Youth Medical Pavilion of Philadelphia
"Spatial genome re-organization between fetal and adult hematopoietic stem cells."

Mei Zhou, Ph.D.
Professor, Department of Genetics
Ellsworth Medical School
"Title of talk TBA."

```html
<!DOCTYPE html>
<html lang="en">
<head>
<meta charset="utf-8">
<title>Lattice and Pathway Biosciences Symposium</title>
<link rel="stylesheet" href="https://fonts.googleapis.com/css2?family=Ubuntu:wght@500;700&family=Source+Sans+3:wght@400;600&family=Michroma&display=swap">
<style>
:root{
  --bg:#e9e9e7;
  --paper:#ffffff;
  --ink:#3a3a3c;
  --red:#d7242f;
  --blue:#3ea2cb;
  --blue-dark:#2a86b0;
  --sponsor-blue:#2b8fc4;
  --tab:#5b5b5d;
  --ring:#7a7a7c;
  --soft:#f1f1f1;
}
*{margin:0;padding:0;box-sizing:border-box}
html,body{width:1200px;height:1200px;overflow:hidden;background:var(--bg)}
body{position:relative;font-family:"Source Sans 3",sans-serif;color:var(--ink)}
.poster{position:absolute;left:190px;top:20px;width:820px;height:1160px;background:var(--paper);overflow:hidden;box-shadow:0 4px 18px rgba(0,0,0,.12)}
.abs{position:absolute}
.hero-art{left:400px;top:0;width:420px;height:440px;background:radial-gradient(ellipse at 65% 40%,#2f86b3 0%,#5fb8cf 30%,#b7e2e6 58%,rgba(255,255,255,0) 78%)}
.title{left:50px;top:38px;font-family:"Ubuntu",sans-serif;font-weight:500;line-height:1.08}
.title .l1{font-size:40px;color:var(--ink);display:block}
.title .l2{font-size:36px;color:var(--red);font-weight:700;display:block}
.sponsor{left:56px;top:142px}
.sponsor h3{font-family:"Ubuntu",sans-serif;font-weight:700;color:var(--sponsor-blue);font-size:17px}
.sponsor p{font-size:21px;line-height:1.2;color:var(--ink)}
.marks{left:385px;top:160px;font-family:"Source Sans 3",sans-serif;font-size:16px;font-weight:600;color:#2d4f8a;line-height:1.9}
.marks span{display:flex;align-items:center;gap:6px}
.marks i{display:inline-block;width:12px;height:12px;background:#2d4f8a;border-radius:50%}
.date{left:62px;top:228px;font-family:"Michroma",sans-serif;font-size:19px;letter-spacing:1px}
.date .k{color:var(--red)}
.venue{left:62px;top:268px;display:flex;gap:10px;font-size:13.5px;line-height:1.3}
.venue b{color:var(--sponsor-blue);font-weight:600}
.keynote-band{left:0;top:0;width:820px;height:1160px}
.photo{border-radius:50%;background:radial-gradient(circle at 50% 40%,#c99a80,#6d4a3a 70%,#3c2a22)}
.keynote-photo{left:52px;top:352px;width:200px;height:200px;border:6px solid #fff;box-shadow:0 0 0 2px var(--red),0 4px 10px rgba(0,0,0,.25)}
.keynote{left:300px;top:410px;color:#fff;font-size:14px;line-height:1.25}
.keynote .label{font-family:"Michroma",sans-serif;font-size:10.5px;letter-spacing:.5px}
.keynote .name{display:inline-block;background:#fff;color:var(--ink);border-radius:14px;padding:2px 14px;margin:8px 0 8px -6px;font-size:15px}
.keynote .name em{font-style:normal;color:var(--red)}
.keynote .talk{margin-top:14px}
.speakers-head{left:452px;top:568px;font-family:"Michroma",sans-serif;font-size:20px}
.speakers-head span{color:var(--red)}
.speaker{position:absolute;width:360px;height:130px}
.speaker .pic{position:absolute;left:0;top:10px;width:112px;height:112px;border:5px solid var(--ring);box-shadow:0 3px 8px rgba(0,0,0,.25)}
.speaker .tab{position:absolute;left:80px;top:0;width:200px;height:26px;background:var(--tab);color:#fff;border-radius:0 13px 13px 0;padding-left:46px;font-size:15px;line-height:26px}
.speaker .info{position:absolute;left:128px;top:36px;width:220px;font-size:13px;line-height:1.2}
.speaker .info .talk{margin-top:12px}
.register{left:40px;top:1040px;width:780px;height:90px;background:var(--blue);border-radius:60px 0 0 0;color:#fff;padding:24px 0 0 50px;display:flex;align-items:flex-start;gap:28px}
.register .main{font-family:"Ubuntu",sans-serif;font-size:21px;font-weight:500;line-height:1.1}
.register .main small{display:block;font-family:"Source Sans 3",sans-serif;font-size:15px;font-weight:400}
.register .note{font-size:13px;padding-top:12px}
.register .note b{font-weight:600}
.register .note .star{color:var(--red);font-size:18px}
</style>
</head>
<body>
<main class="poster">
  <div class="abs hero-art" role="img" aria-label="Illustration of a blue DNA double helix"></div>

  <svg class="abs keynote-band" viewBox="0 0 820 1160" aria-hidden="true">
    <defs>
      <linearGradient id="speakerBg" x1="0" y1="0" x2="0" y2="1">
        <stop offset="0" stop-color="#ededed"/><stop offset="1" stop-color="#ffffff"/>
      </linearGradient>
    </defs>
    <path d="M0,560 C20,450 150,380 300,372 L820,460 L820,620 L0,650 Z" fill="#3ea2cb"/>
    <path d="M0,650 C120,600 300,560 500,548 C650,540 760,560 820,600 L820,1160 L0,1160 Z" fill="url(#speakerBg)"/>
  </svg>

  <h1 class="abs title"><span class="l1">Lattice and Pathway</span><span class="l2">BIOSCIENCES SYMPOSIUM</span></h1>

  <div class="abs sponsor">
    <h3>SPONSORED BY:</h3>
    <p>The Corvale Chromatin Institute and<br>The Department of Bioengineering</p>
  </div>
  <div class="abs marks">
    <span><i></i>Corvale Engineering</span>
    <span><i></i>Corvale Chromatin</span>
  </div>

  <div class="abs date"><span class="k">DATE:</span> JANUARY 8, 2018</div>
  <div class="abs venue">
    <svg width="18" height="24" viewBox="0 0 18 24"><path d="M9 0C4 0 0 4 0 9c0 6 9 15 9 15s9-9 9-15c0-5-4-9-9-9z" fill="#d7242f"/><circle cx="9" cy="9" r="3.5" fill="#fff"/></svg>
    <div><b>Havergill Auditorium, Tarnby Center</b><br>for Applied Discovery, 2175 Orchard Terrace Ave,<br>Philadelphia, PA 19127</div>
  </div>

  <div class="abs photo keynote-photo" role="img" aria-label="Portrait photo of keynote speaker Marthe Quillon"></div>
  <div class="abs keynote">
    <div class="label">KEYNOTE SPEAKER:</div>
    <div class="name"><em>Marthe Quillon</em>, Ph.D.</div>
    <div>NTVO Director General; Professor, Lyceum of Norvane;<br>Director, Genetics and Developmental Biology at Institut Bramoux<br>Lyceum of Norvane, NTVO, Institut Bramoux</div>
    <div class="talk">"Title of talk TBA."</div>
  </div>

  <h2 class="abs speakers-head">THE <span>SPEAKERS:</span></h2>

  <section class="speaker" style="left:55px;top:620px">
    <div class="pic photo" role="img" aria-label="Portrait photo of Lena Drewcott"></div>
    <div class="tab">Lena Drewcott, Ph.D.</div>
    <div class="info">Assistant Professor of Cell and Developmental Biology<br>Halvering State University, HMCS<div class="talk">"Title of talk TBA."</div></div>
  </section>
  <section class="speaker" style="left:65px;top:770px">
    <div class="pic photo" role="img" aria-label="Portrait photo of Paul Marden"></div>
    <div class="tab">Paul Marden, Ph.D.</div>
    <div class="info">Assistant Professor of Genetics<br>Halvering State University, HMCS<div class="talk">"Title of talk TBA."</div></div>
  </section>
  <section class="speaker" style="left:75px;top:915px">
    <div class="pic photo" role="img" aria-label="Portrait photo of Ilse Varga"></div>
    <div class="tab">Ilse Varga, Ph.D.</div>
    <div class="info">Professor, Ostrander University<br>Otto Wenzlau Center for Molecular Medicine<div class="talk">"Title of talk TBA."</div></div>
  </section>
  <section class="speaker" style="left:440px;top:610px">
    <div class="pic photo" role="img" aria-label="Portrait photo of Jun Hao"></div>
    <div class="tab">Jun Hao, Ph.D.</div>
    <div class="info">Professor of<br>Cellular and Molecular Medicine<br>Coastal Meridian University<div class="talk">"Title of talk TBA."</div></div>
  </section>
  <section class="speaker" style="left:450px;top:760px">
    <div class="pic photo" role="img" aria-label="Portrait photo of Wei Lun"></div>
    <div class="tab">Wei Lun, Ph.D.</div>
    <div class="info">Associate Professor of Pediatrics<br>The Youth Medical Pavilion of Philadelphia<div class="talk">"Spatial genome re-organization between fetal and adult hematopoietic stem cells."</div></div>
  </section>
  <section class="speaker" style="left:460px;top:910px">
    <div class="pic photo" role="img" aria-label="Portrait photo of Mei Zhou"></div>
    <div class="tab">Mei Zhou, Ph.D.</div>
    <div class="info">Professor, Department of Genetics<br>Ellsworth Medical School<div class="talk">"Title of talk TBA."</div></div>
  </section>

  <footer class="abs register">
    <div class="main">Register and upload abstracts
      <small>for the symposium at
        <svg width="15" height="15" viewBox="0 0 16 16" style="vertical-align:-2px"><g fill="none" stroke="#fff" stroke-width="1.3"><circle cx="8" cy="8" r="7"/><ellipse cx="8" cy="8" rx="3" ry="7"/><path d="M1 8h14M2.5 4.5h11M2.5 11.5h11"/></g></svg>
        www.qzvmrk.com</small>
    </div>
    <div class="note"><span class="star">*</span> Registration and abstract submission closes on <b>JANUARY 4, 2018.</b></div>
  </footer>
</main>
</body>
</html>
```